Plakat für Fußballturnier-Wochenende
Zielgruppe
Wir sind eine IT-Firma und richten jedes Jahr ein Fußballwochenende / Fußballcup aus. Die Zielgruppe des Plakats sind die Anwohner der Gemeinde.
Aufgabenstellung
An den Ortseingängen der Gemeinde Wendelsau stehen Ortsinformationstafeln welche immer für den Aufzug von aktuellen Veranstaltungen genutzt werden. Dies sind quasi Stahlträger auf welche Plakate aufgezogen werden. Hierfür soll ein Plakat erstellt werden. Ebenfalls soll dies auch in sozialen Medien gestreut werden und im lokalen Wochenblatt (A4
) abgedruckt werden.
Auf dem Plakat soll zu sehen sein:
- Logo Brenner & Kluge Cup
- Logo SpVgg Wendelsau
- 7. Brenner & Kluge Cup (das ist quasi das Dach der Veranstaltung)
- Datum: 07. - 09.06.2024
- Ort: Sportpark Lindenwiese
- Freitag: Elfmeterturnier mit Live-Band
- Samstag: Jugendturnier F- und C- Jugend Vormittags und E-Jugend Nachmittags
- Sonntag: Jugendturnier B- und D- Jugend Vormittags und F3-Jugend Nachmittags
- Logo der Band
- Besucher sind Willkommen; Leibliche Wohl ist gesorgt.
- Der Gras Hintergrund ist Optional - muss nicht zwingend dazu
Informationen von der Firma welche den Druck der großen Plakate ausführt:
Die Schilder sind 110cm x 160cm, wenn sie das auf einer Plane(Banner) haben wollen, kommen noch 8 Ösen rein, 2cm vom Rand. Die Grafik sollte am besten auf Originalgröße angelegt werden und abspeichern als PDF.
Die Dateien sollten auch in einer veränderbaren Form zur Verfügung gestellt werden.

```html
<!DOCTYPE html>
<html lang="de">
<head>
<meta charset="utf-8">
<title>7. Brenner &amp; Kluge Cup – Plakat</title>
<link rel="stylesheet" href="https://fonts.googleapis.com/css2?family=Barlow+Condensed:ital,wght@0,400;0,500;0,600;0,700;1,500;1,700;1,800&display=swap">
<style>
  :root {
    --navy: #14233a;
    --navy-deep: #0d1828;
    --pitch-dark: #1d4a22;
    --pitch: #2f7a2c;
    --green: #4aaa3c;
    --green-bright: #7cc242;
    --white: #ffffff;
    --red: #c8102e;
    --page: #ffffff;
  }
  * { margin: 0; padding: 0; box-sizing: border-box; }
  html, body { width: 1200px; height: 960px; overflow: hidden; background: var(--page); }
  body { font-family: "Barlow Condensed", "Arial Narrow", sans-serif; }

  .poster-stage { position: absolute; left: 286px; top: 20px; width: 627px; height: 920px; }
  .poster {
    position: absolute; left: 0; top: 0; width: 710px; height: 1042px;
    transform: scale(0.883); transform-origin: 0 0;
    overflow: hidden; border: 1px solid #9aa;
  }
  .hero-photo {
    position: absolute; inset: 0;
    background:
      radial-gradient(ellipse 38% 28% at 56% 58%, rgba(225,240,235,0.55), transparent 70%),
      radial-gradient(ellipse 60% 30% at 50% 40%, rgba(160,190,195,0.35), transparent 75%),
      linear-gradient(180deg, #1a2c44 0%, #2c4a5e 30%, #5f8a8a 50%, #3d7a3a 70%, var(--pitch-dark) 100%);
  }
  .shapes { position: absolute; inset: 0; }

  .cup-mark {
    position: absolute; left: 30px; top: 70px; width: 210px;
    display: flex; flex-direction: column; align-items: center; gap: 10px;
    color: var(--white); font-weight: 600; font-size: 21px; letter-spacing: 0.5px; text-align: center; line-height: 1.1;
  }
  .cup-mark .square { width: 66px; height: 66px; background: var(--red); }

  .club-mark {
    position: absolute; right: 30px; top: 45px; width: 130px;
    display: flex; flex-direction: column; align-items: center; gap: 8px;
    color: var(--white); font-weight: 600; font-size: 19px; text-align: center; line-height: 1.05;
  }
  .club-mark .circle { width: 60px; height: 60px; border-radius: 50%; background: var(--green); border: 3px solid var(--white); }

  .headline {
    position: absolute; left: 44px; top: 250px; color: var(--white);
    font-style: italic; text-transform: uppercase;
    text-shadow: 3px 3px 0 rgba(0,0,0,0.25);
  }
  .headline .edition {
    position: absolute; left: 0; top: -10px;
    font-size: 215px; font-weight: 500; line-height: 1; letter-spacing: -10px;
  }
  .headline .title {
    position: absolute; left: 136px; top: 14px;
    font-size: 94px; font-weight: 800; line-height: 0.9; white-space: nowrap;
  }

  .date-band {
    position: absolute; left: 86px; top: 445px; width: 510px; height: 70px;
    background: rgba(18,32,44,0.82); clip-path: polygon(3% 0, 100% 0, 97% 100%, 0 100%);
    display: flex; align-items: center; justify-content: center;
    color: var(--green-bright); font-weight: 800; font-style: italic; font-size: 56px; letter-spacing: -0.5px;
  }

  .band-mark {
    position: absolute; left: 32px; top: 825px; color: var(--white);
    font-weight: 700; font-size: 34px; letter-spacing: 1px; line-height: 1;
  }

  .schedule { position: absolute; left: 332px; top: 786px; color: var(--white); }
  .schedule .day { display: grid; grid-template-columns: 104px 240px; align-items: center; height: 36px; }
  .schedule dt { font-weight: 500; font-size: 24px; }
  .schedule dd { font-size: 14.5px; line-height: 1; font-weight: 500; }
  .schedule dd.lead { font-size: 19px; }

  .venue { position: absolute; left: 31px; top: 932px; color: var(--white); }
  .venue h2 { font-weight: 400; font-size: 39px; line-height: 1; text-transform: uppercase; }
  .venue h2 strong { font-weight: 700; }
  .venue p { font-weight: 500; font-size: 19px; line-height: 1.02; margin-top: 8px; }
</style>
</head>
<body>
<div class="poster-stage">
  <article class="poster">
    <div class="hero-photo" role="img" aria-label="Foto: Fußballspieler in grünen Stutzen mit Ball auf Kunstrasen, Nebel im Hintergrund"></div>

    <svg class="shapes" viewBox="0 0 710 1042" aria-hidden="true">
      <path d="M0 0 H300 C260 120 140 190 0 195 Z" fill="var(--navy-deep)" opacity="0.9"/>
      <path d="M250 0 H710 V20 C560 6 400 6 250 20 Z" fill="var(--green)"/>
      <path d="M0 925 C220 880 480 900 710 985 V1042 H0 Z" fill="var(--green)"/>
    </svg>

    <div class="cup-mark"><span class="square"></span><span>BRENNER &amp; KLUGE CUP</span></div>
    <div class="club-mark"><span class="circle"></span><span>SpVgg Wendelsau</span></div>

    <h1 class="headline">
      <span class="edition">7.</span>
      <span class="title">Brenner &amp;<br>Kluge Cup</span>
    </h1>

    <div class="date-band">07. BIS 09. JUNI 2024</div>

    <div class="band-mark">LINDENKLANG</div>

    <dl class="schedule">
      <div class="day"><dt>Freitag:</dt><dd class="lead">Elfmeterturnier mit Live-Band</dd></div>
      <div class="day"><dt>Samstag:</dt><dd>Jugendturnier F- und C- Jugend Vormittags<br>und E-Jugend Nachmittags</dd></div>
      <div class="day"><dt>Sonntag:</dt><dd>Jugendturnier B- und D- Jugend Vormittags<br>und F3-Jugend Nachmittags</dd></div>
    </dl>

    <section class="venue">
      <h2><strong>Ort:</strong> Sportpark Lindenwiese</h2>
      <p>Wir freuen uns auf Euch! Besucher sind herzlich willkommen.<br>Wir haben außerdem ein leckers Buffet für Euch vorbereitet.</p>
    </section>
  </article>
</div>
</body>
</html>
```